Brightpath Wellness Referral Program

We have recently started a referral program for our clinics and we need a postcard that we can hand our to clients to let them know about the new program.
We are looking for a 4x6" card design that highlights our incentive referral program while visually either showing some of the services we offer, or, conveying a message of health, community, family, etc.
The details of our referral program can be found at:
https://brightpathwellness.ca/about/refer-a-friend.html
We would also like to see somewhere on the card, 2 lines for:
1) Your name: ( new clients name)
2) Referred by: __________
The card can be single or double sided, whatever looks best for design purposes.
Target Market(s)
Ages 20-50, equal men and women
Look and feel
Each slider illustrates characteristics of the customer's brand and the style your logo design should communicate.

```html
<!DOCTYPE html>
<html lang="en">
<head>
<meta charset="utf-8">
<title>Brightpath Wellness – Referral Program Postcard</title>
<link rel="stylesheet" href="https://fonts.googleapis.com/css2?family=Montserrat:ital,wght@0,800;0,900;1,700&family=Roboto:ital,wght@0,400;0,500;0,700;1,400;1,700&display=swap">
<style>
  :root {
    --brand-blue: #0b69ae;
    --brand-blue-deep: #15477d;
    --brand-blue-faint: #3a86c6;
    --silver: #9a9a9a;
    --silver-light: #d9dbde;
    --paper: #ffffff;
    --ink: #2b2b2b;
    --stage: #ececec;
  }
  * { box-sizing: border-box; margin: 0; padding: 0; }
  html, body { width: 1200px; height: 923px; overflow: hidden; background: var(--stage); }
  body { position: relative; font-family: "Roboto", Arial, sans-serif; }

  .postcard {
    position: absolute; left: 270px; width: 660px; height: 440px;
    overflow: hidden; background: var(--paper);
    box-shadow: 0 2px 8px rgba(0,0,0,.18);
  }
  .postcard--front { top: 14px; }
  .postcard--back { top: 470px; }
  .postcard__art { position: absolute; inset: 0; width: 660px; height: 440px; }

  .brand-name {
    position: absolute; display: flex; align-items: center; gap: 8px;
    font-family: "Roboto", Arial, sans-serif; font-weight: 500; white-space: nowrap;
  }
  .brand-name__dot { width: 14px; height: 14px; border-radius: 50%; border: 2px solid currentColor; }
  .postcard--front .brand-name { left: 30px; top: 42px; font-size: 24px; color: var(--paper); }
  .postcard--back .brand-name { left: 450px; top: 390px; font-size: 17px; color: var(--brand-blue); }

  /* Earn badge */
  .earn-badge { position: absolute; text-align: center; color: var(--brand-blue); font-family: "Montserrat", Arial, sans-serif; font-weight: 900; }
  .earn-badge__label { position: absolute; font-size: 15px; line-height: 1; }
  .earn-badge__amount { position: absolute; line-height: 1; letter-spacing: -2px; }

  .postcard--front .earn-badge { left: 345px; top: 335px; width: 170px; height: 105px; }
  .postcard--front .earn-badge__label { right: 38px; top: 14px; font-size: 18px; }
  .postcard--front .earn-badge__amount { left: 18px; top: 28px; font-size: 62px; }

  /* Form lines */
  .referral-form { position: absolute; left: 40px; top: 318px; width: 260px; color: var(--ink); }
  .referral-form__field { font-weight: 700; font-size: 14px; }
  .referral-form__line { border-bottom: 2px dotted #555; height: 14px; margin-bottom: 3px; }
  .referral-form__hint { font-size: 7px; font-style: italic; text-align: center; margin-bottom: 18px; }

  /* Back */
  .announce-tag {
    position: absolute; left: 0; top: 16px; width: 255px; height: 42px;
    padding: 5px 0 0 26px; color: var(--paper);
    font-family: "Montserrat", Arial, sans-serif; font-weight: 900; font-size: 15px; line-height: 16px;
  }
  .program-title {
    position: absolute; left: 22px; top: 62px; color: var(--paper);
    font-family: "Montserrat", Arial, sans-serif; font-weight: 900; font-size: 41px; line-height: 38px;
  }
  .program-motto {
    position: absolute; left: 22px; top: 166px; color: var(--brand-blue-faint);
    font-family: "Montserrat", Arial, sans-serif; font-weight: 900; font-size: 25px; line-height: 24px; opacity: .75;
  }
  .program-intro { position: absolute; left: 287px; top: 44px; width: 345px; color: var(--paper); font-size: 12.5px; line-height: 16.5px; }
  .program-intro p + p { margin-top: 8px; }

  .postcard--back .earn-badge { top: 147px; width: 128px; height: 78px; }
  .earn-badge--south { left: 282px; }
  .earn-badge--north { left: 446px; }
  .postcard--back .earn-badge__label { right: 26px; top: 8px; font-size: 13px; }
  .postcard--back .earn-badge__amount { left: 14px; top: 18px; font-size: 46px; }

  .reward-caption {
    position: absolute; top: 232px; width: 140px; color: var(--paper);
    font-style: italic; font-weight: 700; font-size: 8.6px; line-height: 11px;
  }
  .reward-caption--south { left: 287px; }
  .reward-caption--north { left: 451px; }

  .credit-summary { position: absolute; left: 22px; top: 322px; width: 620px; color: var(--ink); font-size: 12.6px; line-height: 16.6px; }
  .fine-print { position: absolute; left: 22px; top: 381px; width: 420px; color: var(--ink); font-style: italic; font-size: 6.1px; line-height: 7.7px; }
</style>
</head>
<body>

<!-- Front of card -->
<section class="postcard postcard--front" aria-label="Postcard front">
  <svg class="postcard__art" viewBox="0 0 660 440" aria-hidden="false">
    <defs>
      <linearGradient id="frontSky" x1="0" y1="0" x2="0" y2="1">
        <stop offset="0" stop-color="#0b69ae"/>
        <stop offset=".5" stop-color="#0b69ae"/>
        <stop offset="1" stop-color="#f3f7fb"/>
      </linearGradient>
      <linearGradient id="massageTone" x1="0" y1="0" x2="1" y2="1">
        <stop offset="0" stop-color="#1f5f9c"/>
        <stop offset="1" stop-color="#3f86c6"/>
      </linearGradient>
      <linearGradient id="portraitTone" x1="0" y1="0" x2="1" y2="1">
        <stop offset="0" stop-color="#e4e8ec"/>
        <stop offset=".6" stop-color="#cfd9e3"/>
        <stop offset="1" stop-color="#a9c4de"/>
      </linearGradient>
    </defs>
    <rect width="660" height="440" fill="url(#frontSky)"/>
    <rect x="0" y="120" width="320" height="230" fill="url(#massageTone)" opacity=".55"
          role="img" aria-label="Photo of a client relaxing face down during a massage"/>
    <path d="M470 0 C320 60 250 240 340 440 L660 440 L660 0 Z" fill="var(--silver-light)"/>
    <path d="M495 0 C360 60 290 240 370 440 L660 440 L660 0 Z" fill="#ffffff"/>
    <path d="M530 0 C400 60 330 230 410 430 L660 430 L660 0 Z" fill="url(#portraitTone)"
          role="img" aria-label="Photo of a surprised woman holding cash and pointing toward it"/>
    <ellipse cx="430" cy="388" rx="84" ry="54" fill="#ffffff"/>
    <path d="M360 420 C320 380 360 330 440 334 C500 336 515 372 505 392" fill="none" stroke="var(--brand-blue)" stroke-width="5"/>
  </svg>

  <div class="brand-name"><span class="brand-name__dot"></span>Brightpath Wellness</div>

  <div class="earn-badge">
    <span class="earn-badge__label">Earn</span>
    <span class="earn-badge__amount">$25</span>
  </div>

  <div class="referral-form">
    <div class="referral-form__field">Name:</div>
    <div class="referral-form__line"></div>
    <div class="referral-form__hint">(new clients name)</div>
    <div class="referral-form__field">Referred by:</div>
    <div class="referral-form__line"></div>
  </div>
</section>

<!-- Back of card -->
<section class="postcard postcard--back" aria-label="Postcard back">
  <svg class="postcard__art" viewBox="0 0 660 440" aria-hidden="true">
    <defs>
      <linearGradient id="backBlue" x1="0" y1="0" x2="0" y2="1">
        <stop offset="0" stop-color="#0b69ae"/>
        <stop offset=".55" stop-color="#0d63a6"/>
        <stop offset="1" stop-color="#17467a"/>
      </linearGradient>
    </defs>
    <rect width="660" height="440" fill="#ffffff"/>
    <path d="M0 215 C220 320 470 320 660 190 L660 228 C470 345 210 345 0 270 Z" fill="var(--silver)"/>
    <path d="M0 0 H660 V198 C470 305 230 310 0 232 Z" fill="url(#backBlue)"/>
    <path d="M0 16 H244 Q262 16 262 37 Q262 58 244 58 H0 Z" fill="var(--silver)" stroke="#ffffff" stroke-width="2"/>
    <ellipse cx="342" cy="188" rx="62" ry="40" fill="#8a8f96" opacity=".8"/>
    <ellipse cx="348" cy="186" rx="60" ry="38" fill="#ffffff"/>
    <ellipse cx="506" cy="188" rx="62" ry="40" fill="#8a8f96" opacity=".8"/>
    <ellipse cx="512" cy="186" rx="60" ry="38" fill="#ffffff"/>
  </svg>

  <div class="announce-tag">ANNOUNCING OUR<br>NEWLY REDESIGNED</div>
  <h1 class="program-title">REFERRAL<br>PROGRAM</h1>
  <div class="program-motto">GOOD PEOPLE<br>KNOW GOOD<br>PEOPLE</div>

  <div class="program-intro">
    <p>Referrals are the <b>lifeblood</b> of our small business.</p>
    <p>We are <b>incredibly grateful</b> for your trust and recommendations over the years, and we want to show our gratitude. That's why we are introducing an exciting new way to earn more free treatment. Now you can:</p>
  </div>

  <div class="earn-badge earn-badge--south">
    <span class="earn-badge__label">Earn</span>
    <span class="earn-badge__amount">$25</span>
  </div>
  <div class="earn-badge earn-badge--north">
    <span class="earn-badge__label">Earn</span>
    <span class="earn-badge__amount">$10</span>
  </div>

  <p class="reward-caption reward-caption--south">for every referral you make to our south Calgary location (Ridgeview Drive), and;</p>
  <p class="reward-caption reward-caption--north">for every referral you make to our north Calgary location (Maplecrest).</p>

  <p class="credit-summary">Credits can be <b>used for any service at either our north or south location</b> and, in the spirit of community, <b>credits are transferable</b>. Refer 4 people to the south and you could gift someone a $100 gift card! Or, enjoy a well deserved, free treatment yourself.</p>

  <p class="fine-print">*Referral(s) must be brand new client(s) to the Brightpath Wellness Inc. practice, having never booked or attended an appointment at any Brightpath Wellness location. Referral must attend their appointment for you to be eligible for a referral credit. Referral credit value is dependent upon which Brightpath Wellness location your referral attends: you are eligible for a $10 credit for a referral to our north location (#4120 - 1875 Alder Creek Parkway NW); you are eligible for a $25 credit for a referral to our south location (#305 - 6410 Lakeshore Drive SE). We are really good at asking but please remind your referral to tell us it is YOU who we have to thank! Credit(s) may be redeemed as payment or partial payment for any service at any Brightpath Wellness location. Credits have no cash value and no expiry.</p>

  <div class="brand-name"><span class="brand-name__dot"></span>Brightpath Wellness</div>
</section>

</body>
</html>
```